Kelvara Learning Australia - Course Brochure Design

Kelvara Learning Australia is a Private Register Training Organisation that delivery accredited training courses to students. These courses are delivery via face to face training and distance education (e.g. elearning).

We are looking to get a template designed via adobe in design that we can use for each of our courses and list the information relevant for each one.

It will need to be around 3 - 4 pages long to be able to fit the information required into the brochure, i have attached some example of other providers course information sheets.

From the examples you'll be able to see that most of the information will remained the same until it gets to the course structure.

I would like it to be kept within our current theme, we are in the middle of upgrading our new website and look (www.kelvara.com.au/drupal).

I look forward to see what you all come back with.
Updates

Project Deadline Extended
Reason: Hi everyone, Thanks for submitting your design, I have extended the deadline due to not many designs have been submitted. I will be review and providing feedback on the designed submitted this week and will provide some more information based off the work and direction of the designs submitted. Thanks, Pedro.

Target Market(s)

our target market is business and individuals who would like to undergo training course. This brochure needs to display the require information.

Industry/Entity Type

Education

Requirements
Must have
• The brochure must have a front page with a design to list our company logo and information and the course title.

A call to action must be on every page, e.g. footer to enrol now call kelvra on 1800 392 058 or visit www.kelvara.com.au

Nice to have
• Some picture to fill the pages would add a nice look

```html
<!DOCTYPE html>
<html lang="en">
<head>
<meta charset="utf-8">
<title>Kelvara Learning Australia – Aged Care Course Brochure</title>
<link href="https://fonts.googleapis.com/css2?family=Source+Sans+3:wght@300;400;600;700&family=Source+Serif+4:wght@400&display=swap" rel="stylesheet">
<style>
  :root{
    --backdrop:#ececec;
    --paper:#ffffff;
    --navy:#14233a;
    --blue-top:#336f9d;
    --blue-bottom:#1f4f79;
    --numeral:#2a6290;
    --orange:#d8782c;
    --orange-bar:#dc7a26;
    --gold-a:#d8a62b;
    --gold-b:#c9992a;
    --ink:#2b2b2b;
    --code-blue:#2f5f8c;
    --rule:#e4b07a;
    --white:#ffffff;
  }
  *{margin:0;padding:0;box-sizing:border-box}
  html,body{width:1200px;height:900px;overflow:hidden;background:var(--backdrop)}
  .spread{position:absolute;left:25px;top:82px;width:1150px;height:743px;background:var(--paper)}
  .page{position:absolute;top:0;width:575px;height:743px}
  .page--left{left:0}
  .page--right{left:575px}
  .masthead{position:absolute;left:0;top:0;width:575px;height:186px;background:var(--navy)}
  .photo{position:absolute;top:0;height:186px}
  .photo--carer{left:95px;width:433px;background:linear-gradient(135deg,#6f8a5a 0%,#9bb4a8 45%,#5e9ec4 70%,#3d5f3a 100%)}
  .photo--hands{left:48px;width:432px;background:radial-gradient(ellipse at 60% 45%,#d2a89a 0%,#c49586 40%,#e9e6e4 85%)}
  .page-title{position:absolute;left:103px;top:110px;font:700 35px/1 "Source Sans 3",sans-serif;color:var(--white);letter-spacing:.5px}

  .level-numeral{position:absolute;left:50px;font:700 36px/1 "Source Sans 3",sans-serif;color:var(--numeral);letter-spacing:1px}
  .fact-list{position:absolute;left:95px;width:128px;list-style:none}
  .fact{height:45px;margin-bottom:3px;padding:7px 8px 0;background:linear-gradient(180deg,var(--blue-top),var(--blue-bottom));color:var(--white)}
  .fact:last-child{margin-bottom:0}
  .fact__label{display:block;font:600 14px/1.1 "Source Sans 3",sans-serif}
  .fact__value{display:block;font:400 9px/1.4 "Source Sans 3",sans-serif;margin-top:2px}

  .copy{position:absolute;font:400 11.5px/14px "Source Serif 4",serif;color:var(--ink)}
  .copy p{margin-bottom:6px}
  .copy--left{left:245px;top:226px;width:285px}
  .copy--right{left:48px;top:226px;width:285px}
  .section-heading{font:300 18px/1 "Source Sans 3",sans-serif;color:var(--orange);margin:16px 0 8px}
  .roles{list-style:none;margin:6px 0 5px;color:var(--orange)}
  .roles li{line-height:17px}
  .roles li::before{content:"» ";}

  .course-heading{position:absolute;left:48px;top:329px;font:300 18px/1 "Source Sans 3",sans-serif;color:var(--orange)}
  .units{position:absolute;left:48px;top:354px;width:432px;border-collapse:collapse}
  .units th{background:var(--orange-bar);color:var(--white);font:600 14px/21px "Source Sans 3",sans-serif;text-align:left;padding:0 3px}
  .units td{vertical-align:top;padding:4px 3px 3px;border-bottom:1px solid var(--rule);height:41px}
  .units tr:last-child td{border-bottom:none}
  .unit-code{width:76px;font:400 12px/14px "Source Sans 3",sans-serif;color:var(--code-blue)}
  .unit-name{width:130px;font:400 12px/14px "Source Sans 3",sans-serif;color:var(--ink)}
  .unit-desc{font:400 8.5px/11px "Source Serif 4",serif;color:var(--ink)}

  .cta-bar{position:absolute;top:666px;width:433px;height:26px;background:linear-gradient(90deg,var(--gold-a),var(--gold-b));color:var(--white);font:700 14px/26px "Source Sans 3",sans-serif;padding:0 6px}
  .page--left .cta-bar{left:95px}
  .page--right .cta-bar{left:48px;text-align:right}
</style>
</head>
<body>
<main class="spread">
  <section class="page page--left">
    <header class="masthead">
      <div class="photo photo--carer" role="img" aria-label="Nurse in blue scrubs caring for an elderly man in a garden"></div>
      <h1 class="page-title">AGED CARE</h1>
    </header>

    <div class="level-numeral" style="top:228px">III</div>
    <ul class="fact-list" style="top:226px">
      <li class="fact"><span class="fact__label">National Code</span><span class="fact__value">CHC30208</span></li>
      <li class="fact"><span class="fact__label">Course</span><span class="fact__value">Certificate III in Aged Care</span></li>
      <li class="fact"><span class="fact__label">Duration</span><span class="fact__value">12 - 24 Months</span></li>
      <li class="fact" style="height:47px"><span class="fact__label">Availability</span><span class="fact__value">National</span></li>
    </ul>

    <div class="level-numeral" style="top:428px">IV</div>
    <ul class="fact-list" style="top:426px">
      <li class="fact"><span class="fact__label">National Code</span><span class="fact__value">CHC40108</span></li>
      <li class="fact"><span class="fact__label">Course</span><span class="fact__value">Certificate IV in Aged Care</span></li>
      <li class="fact"><span class="fact__label">Duration</span><span class="fact__value">12 - 24 Months</span></li>
      <li class="fact" style="height:53px"><span class="fact__label">Availability</span><span class="fact__value">National</span></li>
    </ul>

    <div class="copy copy--left">
      <p>Depending upon the level of qualification undertaken you will addresses work primarily in residential facilities either under direct or regular supervision, or actually be supervising actions, within clearly defined organisation guidelines and service plans.</p>
      <h2 class="section-heading">What will you achive?</h2>
      <p style="margin-bottom:0">Level III workers may carry out activities to maintain personal care and/or other activities of living for people in an aged care setting, maybe relating to an individualized plan. Occupational titles may include:</p>
      <ul class="roles">
        <li>accommodation support worker</li>
        <li>field officer</li>
        <li>assistant in nursing</li>
        <li>home care assistant</li>
        <li>care assistant</li>
        <li>in-home respite worker</li>
        <li>community, personal or residential care giver</li>
      </ul>
      <p>At certificate IV level you may already, or hope to carry out activities related to maintaining an individual's wellbeing through personal care and/or other activities of living, provide services to individuals with complex needs, and/or work with groups of older people Work may include training and support to promote independence and community</p>
    </div>

    <div class="cta-bar">call Kelvara on 1800 392 058</div>
  </section>

  <section class="page page--right">
    <header class="masthead">
      <div class="photo photo--hands" role="img" aria-label="Close-up of elderly hands clasped together, one wearing a gold ring"></div>
    </header>

    <div class="copy copy--right">
      <p>participation, which may be provided as part of activities and programs in a variety of settings including residential and centre-based programs. Your reporting may include service managers, other professionals and service providers. You may also supervise and/or coordinate a limited number of other workers.</p>
    </div>

    <h2 class="course-heading">Course structure</h2>
    <table class="units">
      <thead>
        <tr><th>Unit Code</th><th>Unit Name</th><th>Description</th></tr>
      </thead>
      <tbody>
        <tr><td class="unit-code">BSBOHS201A</td><td class="unit-name">Participate in OHS processes</td><td class="unit-desc">Participate in workplace occupational health and safety (OHS) processes to protect workers own health and safety, and that of others.</td></tr>
        <tr><td class="unit-code">BSBCUS201A</td><td class="unit-name">Deliver a service to customers</td><td class="unit-desc">Deliver all aspects of customer service at an introductory level. It includes creating a relationship with customers, identifying their needs, delivering services or products and processing customer feedback.</td></tr>
        <tr><td class="unit-code">BSBIND201A</td><td class="unit-name">Work effectively in a business environment</td><td class="unit-desc">Work effectively within a commercial or business environment. It includes identifying the rights and responsibilities of employees and employers and conducting business in accordance with the organisational goals, values and standards.</td></tr>
        <tr><td class="unit-code">BSBINM201A</td><td class="unit-name">Process and maintain workplace information</td><td class="unit-desc">Collect, process, store and maintain workplace information and systems. It alsoincludes the maintenance of filing and records systems.</td></tr>
        <tr><td class="unit-code">BSBCMM201A</td><td class="unit-name">Communicate in the workplace</td><td class="unit-desc">Communicate in the workplace. It includes gathering, conveying and receiving information together with completing routine written correspondence.</td></tr>
        <tr><td class="unit-code">BSBITU201A</td><td class="unit-name">Produce simple word processed documents</td><td class="unit-desc">Correctly operate word processing applications in the production of workplace</td></tr>
      </tbody>
    </table>

    <div class="cta-bar">visit www.kelvara.com.au</div>
  </section>
</main>
</body>
</html>
```